Finance web application design

We need a design for a new responsive finance web application. It should look uber professional and modern.

Inspiration and design we like:

website:
http://www.brennickhale.com/

The application presented here:
http://markets.pelvantgrid.com/en/products/tools-applications/trading-investment-tools/zarvo-trading-software.html

https://apps.quillstore.example/us/app/ferncastle-for-tablet/id582917463?mt=8

The application presented here (Slatepad version):
https://apps.quillstore.example/en/app/trevik-forex-trading/id649205318?mt=8&utm_source=trevikButton

Target Market(s)

Private Investors

Industry/Entity Type

Finance

Number of Pages Required

5+ page

Font styles to use
Other font styles liked:
• Nobile

Requirements
Must have
• Colors for "up" changes: green
• Colors for "down" changes: red
• Fonts in tables must be very easy to read -
• Deliver design for all pages attached.
Nice to have
• A dark (gray) background
• Graphs should be shaded and partly transparent - orange or blue
• White text as "normal" - orange text / blue text for headers
Should not have
• White background

```html
<!DOCTYPE html>
<html lang="en">
<head>
<meta charset="utf-8">
<title>Marketvane – Strategy</title>
<link href="https://fonts.googleapis.com/css2?family=Lato:wght@400;700;900&display=swap" rel="stylesheet">
<style>
:root{
  --page:#3b3e41;
  --shell:#4a4e52;
  --panel:#5b6064;
  --panel-head:#303234;
  --line:#6c7175;
  --grid:#767b80;
  --orange:#f0891c;
  --orange-soft:rgba(240,137,28,.28);
  --text:#f2f2f2;
  --muted:#c9ccce;
  --dark-cell:#3c3f42;
  --up:#5fbf5a;
  --down:#e0584d;
}
*{box-sizing:border-box;margin:0;padding:0}
html,body{width:1200px;height:2368px;overflow:hidden}
body{background:var(--page);font-family:"Lato",sans-serif;color:var(--text);position:relative}

.topbar{position:absolute;left:0;top:0;width:1200px;height:88px;background:var(--orange)}
.brand{position:absolute;left:60px;top:14px;font-size:34px;font-weight:900;color:#fff;display:flex;align-items:center;gap:10px}
.brand-dot{width:22px;height:22px;border-radius:50%;background:#fff}
.nav{position:absolute;left:200px;top:62px;display:flex;gap:6px}
.nav a{display:block;width:112px;height:26px;line-height:26px;text-align:center;font-size:13px;color:#fff;text-decoration:none;background:var(--panel-head)}
.nav a.active{background:var(--page);color:var(--orange);font-weight:700}
.search{position:absolute;left:880px;top:20px;width:150px;height:24px;background:#fff;border:1px solid #ddd;font-size:11px;color:#999;padding:5px 8px}
.signout{position:absolute;left:1040px;top:18px;width:80px;height:28px;background:var(--panel-head);color:var(--orange);font-size:12px;font-weight:700;text-align:center;line-height:28px}

.shell{position:absolute;left:60px;top:120px;width:1080px;height:2240px;background:var(--shell)}
.page-title{position:absolute;left:60px;top:120px;width:1080px;height:60px;background:var(--panel-head);padding:14px 20px;font-size:28px;font-weight:700;color:#fff}

.panel{position:absolute;background:var(--panel)}
.panel-head{height:44px;background:var(--panel-head);padding:13px 18px;font-size:16px;font-weight:700;color:var(--orange)}
.panel svg{display:block}
.axis text{fill:var(--muted);font-size:11px;font-family:"Lato",sans-serif}
.gridline{stroke:var(--grid);stroke-width:1}

.pl-table{margin:26px 20px 0;border-collapse:collapse;width:1000px;font-size:10px}
.pl-table th{background:var(--panel-head);color:#fff;font-weight:700;height:24px}
.pl-table td{height:26px;text-align:center;color:var(--text);border-bottom:1px solid var(--line)}
.pl-table td.year{color:var(--muted)}
.pl-table td.dark{background:var(--dark-cell)}

.stats{width:100%;border-collapse:collapse;font-size:11px}
.stats th{background:var(--panel-head);color:#fff;text-align:left;padding:10px 18px;font-weight:700}
.stats td{padding:0 18px;height:35px;border-bottom:1px solid var(--line);color:var(--text)}
.stats td:last-child{text-align:left}

.positions{width:1000px;margin:0 20px;border-collapse:collapse;font-size:11px}
.positions th{background:var(--panel-head);color:#fff;text-align:left;padding:12px 16px}
.positions td{padding:0 16px;height:42px;border-bottom:1px solid var(--line)}
.show-all{display:block;text-align:right;margin:16px 40px 10px;font-size:11px;color:var(--orange)}
</style>
</head>
<body>

<header class="topbar">
  <div class="brand"><span class="brand-dot"></span>Marketvane</div>
  <nav class="nav">
    <a href="#">Dashboard</a><a href="#" class="active">Strategies</a><a href="#">Portfolios</a><a href="#">Market Data</a><a href="#">Overview</a><a href="#">Users</a>
  </nav>
  <div class="search">Search for assets</div>
  <div class="signout">Sign Out</div>
</header>

<div class="shell"></div>
<h1 class="page-title">Strategy</h1>

<section class="panel" style="left:80px;top:192px;width:1040px;height:250px">
  <div class="panel-head">Profit &amp; Loss</div>
  <table class="pl-table">
    <tr><th>Year</th><th>January</th><th>February</th><th>March</th><th>April</th><th>May</th><th>June</th><th>July</th><th>August</th><th>September</th><th>October</th><th>November</th><th>December</th><th>Compound</th></tr>
    <tr><td class="year">2014</td><td>-1.4%</td><td>-1.2%</td><td class="dark">0.74%</td><td>-1.1%</td><td class="dark">1.04%</td><td class="dark">0.86%</td><td>-0.4%</td><td class="dark">1.12%</td><td>0.79%</td><td class="dark">-1.2%</td><td>-1.0%</td><td class="dark">3.05%</td><td>1.24%</td></tr>
    <tr><td class="year">2015</td><td></td><td></td><td></td><td></td><td></td><td></td><td></td><td></td><td></td><td></td><td></td><td></td><td></td></tr>
    <tr><td class="year">2016</td><td></td><td></td><td></td><td></td><td></td><td></td><td></td><td></td><td></td><td></td><td></td><td></td><td></td></tr>
  </table>
</section>

<section class="panel" style="left:80px;top:472px;width:640px;height:430px">
  <div class="panel-head">Equity Curve</div>
  <svg width="640" height="386" viewBox="0 0 640 386" role="img" aria-label="Equity curve line chart">
    <g class="axis">
      <line class="gridline" x1="80" y1="30" x2="610" y2="30"/><line class="gridline" x1="80" y1="86" x2="610" y2="86"/>
      <line class="gridline" x1="80" y1="142" x2="610" y2="142"/><line class="gridline" x1="80" y1="198" x2="610" y2="198"/>
      <line class="gridline" x1="80" y1="254" x2="610" y2="254"/><line class="gridline" x1="80" y1="310" x2="610" y2="310"/>
      <text x="70" y="34" text-anchor="end">2500000</text><text x="70" y="90" text-anchor="end">2000000</text>
      <text x="70" y="146" text-anchor="end">1500000</text><text x="70" y="202" text-anchor="end">1000000</text>
      <text x="70" y="258" text-anchor="end">500000</text><text x="70" y="314" text-anchor="end">0</text>
      <g text-anchor="middle">
        <text x="90" y="332">Jan</text><text x="124" y="332">Feb</text><text x="159" y="332">Mar</text><text x="193" y="332">Apr</text><text x="227" y="332">May</text><text x="262" y="332">Jun</text><text x="296" y="332">Jul</text><text x="330" y="332">Aug</text><text x="365" y="332">Sep</text><text x="399" y="332">Oct</text><text x="433" y="332">Nov</text><text x="468" y="332">Dec</text><text x="502" y="332">Jan</text><text x="536" y="332">Feb</text><text x="570" y="332">Mar</text><text x="604" y="332">Apr</text>
      </g>
    </g>
    <polygon fill="var(--orange-soft)" points="90,310 90,198 124,175.6 159,158.8 193,164.4 227,142 262,136.4 296,142 330,130.8 365,119.6 399,125.2 433,97.2 468,91.6 502,86 536,63.6 570,69.2 604,58 604,310"/>
    <polyline fill="none" stroke="var(--orange)" stroke-width="3" points="90,198 124,175.6 159,158.8 193,164.4 227,142 262,136.4 296,142 330,130.8 365,119.6 399,125.2 433,97.2 468,91.6 502,86 536,63.6 570,69.2 604,58"/>
    <g fill="var(--orange)">
      <circle cx="90" cy="198" r="4"/><circle cx="124" cy="175.6" r="4"/><circle cx="159" cy="158.8" r="4"/><circle cx="193" cy="164.4" r="4"/><circle cx="227" cy="142" r="4"/><circle cx="262" cy="136.4" r="4"/><circle cx="296" cy="142" r="4"/><circle cx="330" cy="130.8" r="4"/><circle cx="365" cy="119.6" r="4"/><circle cx="399" cy="125.2" r="4"/><circle cx="433" cy="97.2" r="4"/><circle cx="468" cy="91.6" r="4"/><circle cx="502" cy="86" r="4"/><circle cx="536" cy="63.6" r="4"/><circle cx="570" cy="69.2" r="4"/><circle cx="604" cy="58" r="4"/>
    </g>
  </svg>
</section>

<section class="panel" style="left:80px;top:912px;width:640px;height:470px">
  <div class="panel-head">Drawdown</div>
  <svg width="640" height="426" viewBox="0 0 640 426" role="img" aria-label="Drawdown line chart">
    <g class="axis">
      <line class="gridline" x1="80" y1="30" x2="610" y2="30"/><line class="gridline" x1="80" y1="77" x2="610" y2="77"/>
      <line class="gridline" x1="80" y1="124" x2="610" y2="124"/><line class="gridline" x1="80" y1="171" x2="610" y2="171"/>
      <line class="gridline" x1="80" y1="218" x2="610" y2="218"/><line class="gridline" x1="80" y1="265" x2="610" y2="265"/>
      <line class="gridline" x1="80" y1="312" x2="610" y2="312"/><line class="gridline" x1="80" y1="359" x2="610" y2="359"/>
      <text x="70" y="34" text-anchor="end">0</text><text x="70" y="81" text-anchor="end">-10000</text><text x="70" y="128" text-anchor="end">-20000</text><text x="70" y="175" text-anchor="end">-30000</text><text x="70" y="222" text-anchor="end">-40000</text><text x="70" y="269" text-anchor="end">-50000</text><text x="70" y="316" text-anchor="end">-60000</text><text x="70" y="363" text-anchor="end">-70000</text>
      <g text-anchor="middle">
        <text x="90" y="392">Jan</text><text x="124" y="392">Feb</text><text x="159" y="392">Mar</text><text x="193" y="392">Apr</text><text x="227" y="392">May</text><text x="262" y="392">Jun</text><text x="296" y="392">Jul</text><text x="330" y="392">Aug</text><text x="365" y="392">Sep</text><text x="399" y="392">Oct</text><text x="433" y="392">Nov</text><text x="468" y="392">Dec</text><text x="502" y="392">Jan</text><text x="536" y="392">Feb</text><text x="570" y="392">Mar</text><text x="604" y="392">Apr</text>
      </g>
    </g>
    <polygon fill="var(--orange-soft)" points="90,30 124,30 159,30 193,54 227,86 262,218 296,147 330,30 365,171 399,289 433,124 468,372 502,77 536,171 570,30 604,30"/>
    <polyline fill="none" stroke="var(--orange)" stroke-width="3" points="90,30 124,30 159,30 193,54 227,86 262,218 296,147 330,30 365,171 399,289 433,124 468,372 502,77 536,171 570,30 604,30"/>
    <g fill="var(--orange)">
      <circle cx="90" cy="30" r="4"/><circle cx="124" cy="30" r="4"/><circle cx="159" cy="30" r="4"/><circle cx="193" cy="54" r="4"/><circle cx="227" cy="86" r="4"/><circle cx="262" cy="218" r="4"/><circle cx="296" cy="147" r="4"/><circle cx="330" cy="30" r="4"/><circle cx="365" cy="171" r="4"/><circle cx="399" cy="289" r="4"/><circle cx="433" cy="124" r="4"/><circle cx="468" cy="372" r="4"/><circle cx="502" cy="77" r="4"/><circle cx="536" cy="171" r="4"/><circle cx="570" cy="30" r="4"/><circle cx="604" cy="30" r="4"/>
    </g>
  </svg>
</section>

<section class="panel" style="left:740px;top:472px;width:380px;height:910px">
  <div class="panel-head">Statistics</div>
  <table class="stats">
    <tr><th>Name</th><th>Value</th></tr>
    <tr><td>Initial Capital</td><td>1,000,000.0000</td></tr>
    <tr><td>Equity</td><td>2,271,012.0300</td></tr>
    <tr><td>Cash Money</td><td>12,864.0000</td></tr>
    <tr><td>Total Return</td><td>127.10%</td></tr>
    <tr><td>Avg Profit / Trade</td><td>4,611.3400</td></tr>
    <tr><td>Sum Profits</td><td>24</td></tr>
    <tr><td>Max Drawdown</td><td>-80,180.0000</td></tr>
    <tr><td>Max Drawdown Bars</td><td>3</td></tr>
    <tr><td>Profit Drawdown Ratio</td><td>0.51</td></tr>
    <tr><td>Winning Months</td><td>65.0%</td></tr>
    <tr><td>Number Trades</td><td>63</td></tr>
    <tr><td>CAGR</td><td>0.27</td></tr>
    <tr><td>Cumulative Profit Factor</td><td>6.7850</td></tr>
    <tr><td>Min Avg Return/Yr</td><td></td></tr>
    <tr><td>Min Volatility/Yr</td><td></td></tr>
    <tr><td>Min Return/Yr</td><td></td></tr>
    <tr><td>Min Sharpe Ratio</td><td></td></tr>
    <tr><td>Risk Free Rate</td><td></td></tr>
    <tr><td>Ulcer Performance</td><td></td></tr>
    <tr><td>Sharpe Ratio</td><td>0.85</td></tr>
    <tr><td>Alpha</td><td></td></tr>
    <tr><td>Expected Shortfall</td><td></td></tr>
    <tr><td>Sortino Ratio</td><td>1.36</td></tr>
  </table>
</section>

<section class="panel" style="left:80px;top:1400px;width:640px;height:262px">
  <div class="panel-head">Market Timing</div>
  <svg width="640" height="218" viewBox="0 0 640 218" role="img" aria-label="Market timing bar chart">
    <g class="axis">
      <line class="gridline" x1="60" y1="30" x2="610" y2="30"/><line class="gridline" x1="60" y1="70" x2="610" y2="70"/><line class="gridline" x1="60" y1="110" x2="610" y2="110"/><line class="gridline" x1="60" y1="150" x2="610" y2="150"/><line class="gridline" x1="60" y1="190" x2="610" y2="190"/>
      <text x="50" y="34" text-anchor="end">1</text><text x="50" y="194" text-anchor="end">0</text>
    </g>
    <g fill="var(--orange)">
      <rect x="84" y="30" width="12" height="160"/><rect x="118" y="30" width="12" height="160"/><rect x="152" y="30" width="12" height="160"/><rect x="186" y="30" width="12" height="160"/><rect x="220" y="30" width="12" height="160"/><rect x="254" y="30" width="12" height="160"/><rect x="288" y="30" width="12" height="160"/><rect x="322" y="30" width="12" height="160"/><rect x="356" y="30" width="12" height="160"/><rect x="390" y="30" width="12" height="160"/><rect x="492" y="30" width="12" height="160"/><rect x="526" y="30" width="12" height="160"/><rect x="560" y="30" width="12" height="160"/><rect x="594" y="30" width="12" height="160"/>
    </g>
    <g class="axis" text-anchor="middle">
      <text x="90" y="210">Jan</text><text x="124" y="210">Feb</text><text x="158" y="210">Mar</text><text x="192" y="210">Apr</text><text x="226" y="210">May</text><text x="260" y="210">Jun</text><text x="294" y="210">Jul</text><text x="328" y="210">Aug</text><text x="362" y="210">Sep</text><text x="396" y="210">Oct</text><text x="430" y="210">Nov</text><text x="464" y="210">Dec</text><text x="498" y="210">Jan</text><text x="532" y="210">Feb</text><text x="566" y="210">Mar</text><text x="600" y="210">Apr</text>
    </g>
  </svg>
</section>

<section class="panel" style="left:80px;top:1680px;width:640px;height:302px">
  <div class="panel-head">Number Instruments passing filter</div>
  <svg width="640" height="258" viewBox="0 0 640 258" role="img" aria-label="Instruments passing filter bar chart">
    <g class="axis">
      <line class="gridline" x1="60" y1="30" x2="610" y2="30"/><line class="gridline" x1="60" y1="65" x2="610" y2="65"/><line class="gridline" x1="60" y1="100" x2="610" y2="100"/><line class="gridline" x1="60" y1="135" x2="610" y2="135"/><line class="gridline" x1="60" y1="170" x2="610" y2="170"/><line class="gridline" x1="60" y1="205" x2="610" y2="205"/><line class="gridline" x1="60" y1="230" x2="610" y2="230"/>
      <text x="50" y="34" text-anchor="end">6</text><text x="50" y="69" text-anchor="end">5</text><text x="50" y="104" text-anchor="end">4</text><text x="50" y="139" text-anchor="end">3</text><text x="50" y="174" text-anchor="end">2</text><text x="50" y="209" text-anchor="end">1</text>
    </g>
    <g fill="var(--orange)">
      <rect x="84" y="65" width="12" height="165"/><rect x="118" y="100" width="12" height="130"/><rect x="152" y="100" width="12" height="130"/><rect x="186" y="135" width="12" height="95"/><rect x="220" y="100" width="12" height="130"/><rect x="254" y="30" width="12" height="200"/><rect x="288" y="30" width="12" height="200"/><rect x="322" y="135" width="12" height="95"/><rect x="356" y="65" width="12" height="165"/><rect x="390" y="135" width="12" height="95"/><rect x="424" y="170" width="12" height="60"/><rect x="458" y="135" width="12" height="95"/><rect x="492" y="100" width="12" height="130"/><rect x="526" y="30" width="12" height="200"/><rect x="560" y="65" width="12" height="165"/><rect x="594" y="100" width="12" height="130"/>
    </g>
    <g class="axis" text-anchor="middle">
      <text x="90" y="250">Jan</text><text x="124" y="250">Feb</text><text x="158" y="250">Mar</text><text x="192" y="250">Apr</text><text x="226" y="250">May</text><text x="260" y="250">Jun</text><text x="294" y="250">Jul</text><text x="328" y="250">Aug</text><text x="362" y="250">Sep</text><text x="396" y="250">Oct</text><text x="430" y="250">Nov</text><text x="464" y="250">Dec</text><text x="498" y="250">Jan</text><text x="532" y="250">Feb</text><text x="566" y="250">Mar</text><text x="600" y="250">Apr</text>
    </g>
  </svg>
</section>

<section class="panel" style="left:80px;top:2020px;width:1040px;height:320px">
  <div class="panel-head">Open Positions</div>
  <a class="show-all" href="#">Show all</a>
  <table class="positions">
    <tr><th>Name</th><th>ISIN</th><th>Quantity</th><th>Date</th></tr>
    <tr><td>Arvell Consumer Retail Index NR USD</td><td>QV7301458826</td><td>360</td><td>2015-12-18</td></tr>
    <tr><td>Holdberg Grid AG</td><td>QV7302916640</td><td>124</td><td>2015-12-18</td></tr>
    <tr><td>Corvane Steel Holdings</td><td>QV7305283174</td><td>406</td><td>2015-12-18</td></tr>
  </table>
</section>

</body>
</html>
```